Mechanical Engineer Business Card Design (Unemployed)

I am unemployed and actively looking for a job in Canada. I will be using this business card when I meet potential employers or in networking events.I would love to have the engraved writing style (as if it is engraved on the card). Some examples attached.I would love to have a personalized logo that represents my 2 majors. The final design should have a professional look that can stand out if attached to a resume. Jobs I am applying for are in construction, mining, oil and gas, Aerospace, manufacturing and whatever field I can be integrated in.A metallic look on the back is ok. but the front have to be sort of can be written on. you can also try to add my linkedin profile https://ca.folionet.example/in/doruvelsh
On the front or back, I would love to have the symbol of mail and phone rather than the words. that saves spaceAmaze me guys.

Target Market(s)

Engineering

Industry/Entity Type

Engineering

Contact Information for Business Card

Doru Velsh
Mechanical Engineer

Phone number: +1 (555) 014 - 2736
email: velshdoru@mailbrook.example

Font styles to use
Serif
Sans Serif
Decorative
Script

Requirements
Must have
• PERSONALIZED and brand new Simple Logo
• Professional look
• Engraved writing for the name
• Help stand out when attached on CV
Nice to have
• Metallic back look

```html
<!DOCTYPE html>
<html lang="en">
<head>
<meta charset="utf-8">
<title>Doru Velsh — Business Card</title>
<link href="https://fonts.googleapis.com/css2?family=Merriweather:wght@400;700&display=swap" rel="stylesheet">
<style>
  :root {
    --backdrop: #dddcdc;
    --card-dark: #000000;
    --card-light: #ffffff;
    --ink: #111111;
    --ink-soft: #2a2a2a;
    --paper-text: #ffffff;
    --faint-mark: #efeeee;
    --shadow: rgba(0,0,0,0.18);
  }
  html, body {
    margin: 0;
    padding: 0;
    width: 1200px;
    height: 1189px;
    overflow: hidden;
    background: var(--backdrop);
    font-family: "Merriweather", Georgia, serif;
  }
  .canvas {
    position: relative;
    width: 1200px;
    height: 1189px;
  }
  .card {
    position: absolute;
    width: 700px;
    height: 400px;
    box-shadow: 0 10px 28px var(--shadow);
    overflow: hidden;
  }
  /* Front side */
  .card--front {
    left: 90px;
    top: 110px;
    background: var(--card-dark);
  }
  .front-brand {
    position: absolute;
    left: 230px;
    top: 150px;
    display: flex;
    align-items: center;
    gap: 22px;
  }
  .brand-mark {
    width: 96px;
    height: 96px;
    border-radius: 50%;
  }
  .card--front .brand-mark { background: var(--paper-text); }
  .front-name {
    color: var(--paper-text);
    font-size: 28px;
    font-weight: 400;
    letter-spacing: 1px;
    margin: 0;
  }
  /* Back side */
  .card--back {
    left: 410px;
    top: 660px;
    background: var(--card-light);
  }
  .faint-mark {
    position: absolute;
    width: 250px;
    height: 250px;
    border-radius: 50%;
    border: 60px solid var(--faint-mark);
    box-sizing: border-box;
    right: 40px;
    top: -30px;
  }
  .back-brand {
    position: absolute;
    left: 90px;
    top: 150px;
    display: flex;
    align-items: flex-start;
    gap: 22px;
  }
  .card--back .brand-mark { background: var(--ink); margin-top: 4px; }
  .back-name {
    margin: 0;
    font-size: 28px;
    font-weight: 400;
    color: var(--ink);
    line-height: 1.05;
  }
  .back-role {
    margin: 2px 0 14px;
    font-size: 12px;
    color: var(--ink-soft);
  }
  .degree {
    margin: 0 0 4px 14px;
    font-size: 12.5px;
    color: var(--ink-soft);
  }
  .contact-list {
    position: absolute;
    right: 40px;
    bottom: 78px;
    list-style: none;
    margin: 0;
    padding: 0;
    font-size: 12.5px;
    color: var(--ink);
  }
  .contact-list li {
    display: flex;
    align-items: center;
    gap: 8px;
    margin-bottom: 4px;
  }
  .contact-icon {
    width: 15px;
    height: 15px;
    background: var(--ink);
    display: inline-flex;
    align-items: center;
    justify-content: center;
    flex: none;
  }
</style>
</head>
<body>
<main class="canvas">
  <section class="card card--front" aria-label="Card front">
    <div class="front-brand">
      <span class="brand-mark" aria-hidden="true"></span>
      <h1 class="front-name">Doru Velsh</h1>
    </div>
  </section>

  <section class="card card--back" aria-label="Card back">
    <span class="faint-mark" aria-hidden="true"></span>
    <div class="back-brand">
      <span class="brand-mark" aria-hidden="true"></span>
      <div class="identity">
        <h2 class="back-name">Doru Velsh</h2>
        <p class="back-role">Field Mechanical Engineer</p>
        <p class="degree">Mechanical Engineer (B.Sc.)</p>
        <p class="degree">Aerospace Engineer (M.Sc.)</p>
      </div>
    </div>
    <ul class="contact-list">
      <li>
        <span class="contact-icon">
          <svg width="11" height="11" viewBox="0 0 24 24" aria-hidden="true"><path fill="#fff" d="M6.6 10.8a15.1 15.1 0 0 0 6.6 6.6l2.2-2.2c.3-.3.7-.4 1-.2 1.1.4 2.3.6 3.6.6.6 0 1 .4 1 1V20c0 .6-.4 1-1 1A17 17 0 0 1 3 4c0-.6.4-1 1-1h3.5c.6 0 1 .4 1 1 0 1.3.2 2.5.6 3.6.1.3 0 .7-.2 1l-2.3 2.2z"/></svg>
        </span>
        (+1) 555 - 014 - 2736
      </li>
      <li>
        <span class="contact-icon">
          <svg width="11" height="11" viewBox="0 0 24 24" aria-hidden="true"><path fill="#fff" d="M2 5h20v14H2z"/><path fill="none" stroke="#000" stroke-width="2" d="M2 5l10 8 10-8"/></svg>
        </span>
        velshdoru@mailbrook.example
      </li>
      <li>
        <span class="contact-icon" aria-hidden="true"></span>
        https://ca.folionet.example/in/doruvelsh
      </li>
    </ul>
  </section>
</main>
</body>
</html>
```